Flyer promoting Veltrane's workshops and credentials

We run Training workshops for the data analyst community. We'd like a flyer to sell our services using a style and colour scheme consistent with our website www.veltranepartners.co.uk . I've attached some background info and some existing e-brochures for different workshops to give a flavour for content (but these are poorly designed and we don't want a similar design!!). There's also an overview document which gives more direction. The flyer will be sent with an accompanying letter to Learning & Development decision makers as well as Anlaytical team managers. It's purpose would be to generate enquiries and bookings for primarliy our flagship workshop 'Turning Figures Into Real Gains'.

Target Market(s)

Learning and Development senior managers
Analytical team managers

Industry/Entity Type

Training

Other font styles liked:
• Similar to website for consistency

Requirements
Must have
• Good copy! Slick design more in line with European (UK) style advertising rather than US.
Nice to have
• Some humour,
Should not have
• should not be as boring and non-sales based as the website!! Website is not a great example!

```html
<!DOCTYPE html>
<html lang="en">
<head>
<meta charset="utf-8">
<title>Veltrane – Workshops for Data Analysts</title>
<link rel="stylesheet" href="https://fonts.googleapis.com/css2?family=Arimo:ital,wght@0,400;0,500;0,700;1,400&display=swap">
<style>
:root{
  --navy:#1d3a6e;
  --band:#1f4380;
  --band-dark:#16305d;
  --orange:#f5871f;
  --orange-title:#ee8a2a;
  --blue-title:#2b5c9e;
  --ink:#333;
  --muted:#555;
  --rule:#c9ccd2;
  --panel:#e9ecf2;
  --paper:#fff;
}
*{box-sizing:border-box;margin:0;padding:0}
html,body{width:1200px;height:849px;overflow:hidden;background:var(--paper)}
body{font-family:"Arimo",Arial,sans-serif;color:var(--ink);position:relative}
.page{position:absolute;top:0;width:600px;height:849px;overflow:hidden;background:var(--paper)}
.page--left{left:0}
.page--right{left:600px;border-left:1px solid #888}
.abs{position:absolute}
.brand{left:30px;top:26px;display:flex;flex-direction:column}
.brand__name{font-size:37px;font-weight:700;color:var(--navy);letter-spacing:-1px;line-height:1;display:flex;align-items:center;gap:6px}
.brand__dot{width:11px;height:11px;border-radius:50%;background:var(--orange)}
.brand__tag{font-size:11.5px;font-weight:700;color:var(--orange);margin-left:52px;margin-top:3px}
.site-url{right:30px;top:29px;font-size:11.5px;color:var(--ink)}
.hero-band{left:0;top:90px;width:600px;height:256px;background:linear-gradient(100deg,var(--band-dark) 0%,var(--band) 55%,#3a66a8 100%)}
.hero-rule{left:0;top:346px;width:600px;height:5px;background:var(--orange)}
.hero-circle{left:380px;top:136px;width:176px;height:176px;border-radius:50%;background:var(--orange)}
.hero-photo{left:400px;top:54px;width:200px;height:292px;background:linear-gradient(180deg,rgba(214,170,140,.45),rgba(120,90,70,.3));border-radius:90px 90px 0 0}
.hero-title{left:30px;top:155px;width:320px;font-size:26.4px;font-weight:400;line-height:32px;color:#fff}
.hero-title strong{font-weight:700}
.intro{left:30px;top:379px;width:322px;font-size:9.9px;line-height:14px;color:var(--ink)}
.intro p{margin-bottom:6px}
.intro .offer{font-weight:700}
.intro .offer span{font-weight:400}
.intro .url{font-size:12px}
.col-divider{width:1px;background:var(--rule)}
.testimonials__lead{left:390px;top:380px;width:182px;font-size:14.6px;font-weight:400;line-height:19.2px;color:var(--blue-title)}
.quote{left:390px;width:180px;border-top:2px solid var(--orange);padding-top:10px}
.quote p{font-size:9.4px;line-height:13.2px;font-style:italic;color:var(--muted)}
.quote cite{display:block;text-align:right;font-style:normal;font-size:10px;color:var(--ink);margin-top:2px}
.footer{left:20px;top:801px;width:562px;border-top:2px solid var(--navy);padding:10px 10px 0;display:flex;align-items:center;font-size:10px;color:var(--ink)}
.footer__co{font-size:12px;color:var(--blue-title);margin-right:18px}
.footer__sep{margin:0 14px;color:#666}
.footer__mail{margin-left:auto}
.title-band{left:0;top:90px;width:600px;height:80px;background:linear-gradient(100deg,var(--band-dark),var(--band) 60%,#3a66a8)}
.title-rule{left:0;top:170px;width:600px;height:5px;background:var(--orange)}
.title-band h1{position:absolute;left:30px;top:42px;font-size:26px;font-weight:700;color:#fff;line-height:1}
.desk-photo{left:387px;top:72px;width:183px;height:150px;background:linear-gradient(135deg,#d9dee6,#aebdd2 60%,#7d93b5);box-shadow:0 1px 4px rgba(0,0,0,.3)}
.lead{left:30px;top:200px;width:315px;font-size:12px;line-height:16.8px;color:var(--ink)}
.workshop{left:20px;width:342px;padding:8px 10px}
.workshop--featured{background:var(--panel)}
.workshop__head{display:flex;justify-content:space-between;align-items:center;margin-bottom:8px}
.workshop__title{font-size:12px;font-weight:700;letter-spacing:.2px;text-transform:uppercase}
.workshop__title--blue{color:var(--blue-title)}
.workshop__title--orange{color:var(--orange-title)}
.badge{font-size:11.5px;font-weight:700;color:#fff;padding:3px 5px 3px 12px;clip-path:polygon(6px 0,100% 0,100% 100%,0 100%,0 60%,6px 40%)}
.badge--navy{background:var(--navy)}
.badge--orange{background:var(--orange)}
.workshop__text{font-size:9.8px;line-height:13.8px;color:var(--ink)}
.side-quote{left:390px;width:180px}
.side-quote p{font-size:9.3px;line-height:13.2px;font-style:italic;color:var(--muted)}
.side-quote cite{display:block;text-align:right;font-style:normal;font-size:10px;color:var(--ink);margin-top:2px}
.side-rule{left:390px;width:180px;height:2px;background:var(--orange)}
</style>
</head>
<body>

<section class="page page--left">
  <div class="abs brand">
    <div class="brand__name"><span class="brand__dot"></span>Veltrane</div>
    <div class="brand__tag">Workshops for Data Analysts</div>
  </div>
  <div class="abs site-url">www.veltranepartners.co.uk</div>

  <div class="abs hero-band" role="img" aria-label="Blue-toned background of an analyst's desk with printed charts"></div>
  <div class="abs hero-circle"></div>
  <div class="abs hero-photo" role="img" aria-label="Photo of a smiling young data analyst"></div>
  <div class="abs hero-rule"></div>
  <h2 class="abs hero-title">Do you want your data analysts to have a greater impact on your organisation and be more <strong>productive?</strong></h2>

  <div class="abs intro">
    <p>Veltrane understand that technical ability alone is not enough to be effective as a data analyst. Whether you're an insight expert, a risk analyst or a Business Intelligence professional , the best analysts employ a range of complimentary soft skills in order to be able to effectively plan, present and communicate ideas, results and reports. Our range of workshops aim to help analysts become more commercially focussed and employ some key techniques and behaviours in order to maximise their influence over their key decision makers.</p>
    <p>Our workshops have been attended by many of the UK's largest organisations and many international organisations too including Corvane, Brightmoor Bank, Petravon and Halden Group. Our workshops are run by experienced professionals including Martin Ashcombe, Veltrane's founder and the facilitator for Veltrane's flagship workshop 'Turning Figures Into Real Gains' - a workshop that has been running for over 10 years and become an essential 'cornerstone' development session for many of our regular clients' analysts.</p>
    <p>We run a schedule of open public workshops as well as privately hosted workshops. We can also tailor the content to your specific requirement if necessary. So, whatever your budget we can usually deliver a programme that will fit your needs.</p>
    <p class="offer">Any bookings made with reference to this flyer will benefit from a 10% discount on fees until February 18th 2016 <span>(this may not be used in conjunction with any other promotional rates that may be available at the time of booking).</span></p>
    <p>Our current portfolio of workshops is provided overleaf but more detail and a list of currently scheduled open workshops can be found on the website at <span class="url">www.veltranepartners.co.uk.</span></p>
  </div>

  <div class="abs col-divider" style="left:370px;top:382px;height:406px"></div>

  <p class="abs testimonials__lead">We aim for our workshops to be educational, interactive, practical and fun – we believe we deliver on this but don't just take our word for it, here are some comments from our clients..</p>
  <blockquote class="abs quote" style="top:531px"><p>A very useful course with a very engaging trainer. Excellent examples that related to our work.</p><cite>— Delegate, Linkway Rail</cite></blockquote>
  <blockquote class="abs quote" style="top:611px"><p>"Excellent balance of approach, attitude and methodology with technical competency based analysis techniques. Provides clear framework for universal practice within an analytical team."</p><cite>— Owen Farley, Herald Press Group</cite></blockquote>
  <blockquote class="abs quote" style="top:721px"><p>"Kept me engaged throughout. Exercises were enjoyable and relevant. Easy to process/understand/remember."</p><cite>— Neil Parrott, Chattersea</cite></blockquote>

  <footer class="abs footer">
    <span class="footer__co">Veltrane Partners Ltd</span>|
    <span class="footer__sep">Tel: 0161 555 0142</span>|
    <span class="footer__sep">Fax: 0845 5550199</span>|
    <span class="footer__mail">Email: info@veltranepartners.co.uk</span>
  </footer>
</section>

<section class="page page--right">
  <div class="abs brand">
    <div class="brand__name"><span class="brand__dot"></span>Veltrane</div>
    <div class="brand__tag">Workshops for Data Analysts</div>
  </div>
  <div class="abs site-url">www.veltranepartners.co.uk</div>

  <div class="abs title-band"><h1>Workshops &amp; Seminars</h1></div>
  <div class="abs title-rule"></div>
  <div class="abs desk-photo" role="img" aria-label="Photo of hands pointing at a tablet showing charts"></div>

  <p class="abs lead">Veltrane's workshops are interactive and practical. Delegates can attend one of the scheduled public workshops or if you have several analysts, an on-site private workshop offers significant savings and the chance to work through challenges as a team.</p>

  <div class="abs col-divider" style="left:371px;top:200px;height:580px"></div>

  <article class="abs workshop workshop--featured" style="top:304px">
    <div class="workshop__head"><h3 class="workshop__title workshop__title--blue">Turning Figures Into Real Gains</h3><span class="badge badge--navy">2 Days</span></div>
    <p class="workshop__text">A CPD accredited, interactive soft-skills workshop to improve the productivity and impact an analyst has on the organisation they support. Focusing on the three core themes of Communication, Presentation of Data and Planning.</p>
  </article>
  <article class="abs workshop" style="top:412px">
    <div class="workshop__head"><h3 class="workshop__title workshop__title--orange">Delivering Analysis for Impact</h3><span class="badge badge--orange">.5 Day</span></div>
    <p class="workshop__text">A half day seminar on the key behaviours and techniques information analysts/insight specialists need to employ in order to have a positive impact on their internal or external customers.</p>
  </article>
  <article class="abs workshop" style="top:503px">
    <div class="workshop__head"><h3 class="workshop__title workshop__title--blue">Influencing Skills</h3><span class="badge badge--navy">1 Day</span></div>
    <p class="workshop__text">This workshop equips the analyst with a set of established techniques and principals to help them effectively influence their customers and internal decision makers - a key skill to ensuring personal and commercials goals are achieved.</p>
  </article>
  <article class="abs workshop" style="top:605px">
    <div class="workshop__head"><h3 class="workshop__title workshop__title--orange">Analytics in Direct Marketing</h3><span class="badge badge--orange">1 Day</span></div>
    <p class="workshop__text">A workshop to help delegates understand the tactical and strategic analytics which support the direct marketing life cycle. Includes practical exercises to reinforce the learnings. This worshop can only be hosted privately.</p>
  </article>
  <article class="abs workshop" style="top:704px">
    <div class="workshop__head"><h3 class="workshop__title workshop__title--blue">Tailored Statistical Workshops</h3><span class="badge badge--navy">1 Day</span></div>
    <p class="workshop__text">Customisable workshops - select the statistical methods and techniques you and your colleagues would like to cover and we'll provide you with a tailored day with practical examples and accompanying notes.</p>
  </article>

  <blockquote class="abs side-quote" style="top:250px"><p>"We took from the course a number of actionable learnings that we have put into practice and this has resulted in positive feedback and a happier more valued team. Recommend the course to new and experienced analysts alike."</p><cite>— Dan Meadows, Harvestaid</cite></blockquote>
  <div class="abs side-rule" style="top:355px"></div>
  <blockquote class="abs side-quote" style="top:366px"><p>"Turning Figures Into Real Gains is a high quality, well-structured course delivered by a skilled and knowledgeable trainer. It has provided our analysts with the invaluable customer-focussed skills and techniques that have added value to the whole of the marketing process and a new and original dimension to the career development of our analysis teams."</p><cite>— Graham Tolley, Mutual Union Financial Services</cite></blockquote>
  <div class="abs side-rule" style="top:529px"></div>
  <blockquote class="abs side-quote" style="top:541px"><p>"I really enjoyed the session. It was pitched well for the skill set of attendees. I got a lot out of it in respect of tables/visuals formatting and have totally re-thought my intial views of providing/producing data for my customers. Thankyou."</p><cite>— Priya Castell, Norbeck Systems</cite></blockquote>
  <div class="abs side-rule" style="top:664px"></div>
  <blockquote class="abs side-quote" style="top:677px"><p>"Excellent &amp; relevant exercises. All exercise solutions supplied so no need to worry about interpreting scribbled calcualtions. Pace good and good help available when stuck. Covered all areas I was expecting."</p><cite>— Emma Ridgeway, Harvestaid</cite></blockquote>

  <footer class="abs footer">
    <span class="footer__co">Veltrane Partners Ltd</span>|
    <span class="footer__sep">Tel: 0161 555 0142</span>|
    <span class="footer__sep">Fax: 0845 5550199</span>|
    <span class="footer__mail">Email: info@veltranepartners.co.uk</span>
  </footer>
</section>

</body>
</html>
```